MARBLEQUILL Non-Profit- Pitch Deck needs visual boost

PLEASE CHECK FILE 6 for most current version of Pitch Deck that needs editing. Made some final edits compared to first one uploaded yesterday.

We need to have someone come in and inject our pitch deck with some design and graphic love. The content and words are there but we need it to look sharper, cleaner, and more visually striking. The Non-profit is managing the cleanup of 360 million tonnes of CO2 before the year 2025. We need it to be editable and customizable moving forward so no PDF versions, PP and Keynote only. Please ignore scatch notes after pg 15 .

attachted ex summary in additional uploads for more information.
Check out website too 7386.com

Target Market(s)

Potential partners and investors

Industry/Entity Type

Sustainability

Font styles to use
Sans Serif

Colors

Designer to choose colors to be used in the design.

Requirements
Must have
• Simplified version of current slideshow- Less noise in the deck espcially on logo page.
• Copyright version must be easily editable. Not adobe. PP or Keynote

```html
<!DOCTYPE html>
<html lang="en">
<head>
<meta charset="utf-8">
<title>MarbleQuill Pitch Deck Pages</title>
<link href="https://fonts.googleapis.com/css2?family=Montserrat:wght@400;500;600;700&display=swap" rel="stylesheet">
<style>
:root{
  --bg:#e6e7e8;
  --page:#ffffff;
  --ink:#222222;
  --muted:#666a6e;
  --green:#1e9b57;
  --teal:#14937e;
  --blue:#2a9fd8;
  --orange:#f3a51c;
  --royal:#3a7bd5;
  --lime:#6fd38a;
  --purple:#8e2fb8;
  --red:#e5472f;
  --mist:#d9dcdf;
}
*{box-sizing:border-box;margin:0;padding:0}
html,body{width:1200px;height:1200px;overflow:hidden;background:var(--bg);font-family:'Montserrat',sans-serif;color:var(--ink)}
.deck{position:relative;width:1200px;height:1200px}
.page{position:absolute;width:246px;height:349px;background:var(--page);overflow:hidden;box-shadow:0 1px 3px rgba(0,0,0,.12)}
.page .mist{position:absolute;left:0;right:0;bottom:0;height:150px;background:linear-gradient(180deg,rgba(255,255,255,0) 0%,var(--mist) 55%,#eceeef 100%)}
.abs{position:absolute}
.head-bar{position:absolute;left:0;top:22px;width:4px;height:20px;background:var(--ink)}
.head{position:absolute;left:12px;top:24px;width:190px;font-size:6.3px;font-weight:700;line-height:1.3}
.tag{position:absolute;right:12px;top:22px;width:28px;text-align:center;font-size:3.5px;font-weight:600;color:var(--green)}
.tag i{display:block;width:9px;height:9px;margin:0 auto 2px;border:1.4px solid currentColor;border-radius:50%}
.foot{position:absolute;left:0;right:0;bottom:12px;height:10px}
.foot .bar{position:absolute;left:0;top:-2px;width:4px;height:12px;background:var(--ink)}
.foot .url{position:absolute;left:12px;top:2px;font-size:4.4px;font-weight:600}
.foot .brand{position:absolute;right:18px;top:0;font-size:7px;font-weight:700}
.tiny{font-size:3.6px;line-height:1.45;color:var(--muted)}
.small{font-size:4.6px;line-height:1.4}
.green{color:var(--green)}
.bold{font-weight:700}
.card{position:absolute;background:#fff;border-radius:6px;box-shadow:0 1px 4px rgba(0,0,0,.15)}
.ph{position:absolute;border-radius:3px}
.chip{position:absolute;background:#c9ccd0;border-radius:2px}
</style>
</head>
<body>
<div class="deck">

<section class="page" style="left:175px;top:52px">
  <div class="mist"></div>
  <div class="head-bar"></div>
  <div class="head">We are developing a convenient emissions footprint tracker for the mass market with our tech partners</div>
  <div class="tag"><i></i>Integrate</div>
  <div class="abs small green" style="left:12px;top:46px;font-size:4px;font-style:italic;font-weight:600">“You’re on track to reduce your CO2 impact by 12%<br>this month, and 50% this year!”</div>
  <div class="abs small" style="left:0;right:0;top:78px;text-align:center;font-size:4.4px;font-weight:600">App automatically analyzes spending &amp; GPS to extract CO2e insights...</div>
  <svg class="abs" style="left:18px;top:88px" width="210" height="34" viewBox="0 0 210 34">
    <g fill="none" stroke="#1e9b57" stroke-width="1.1">
      <circle cx="17" cy="17" r="14"/><circle cx="60" cy="17" r="14"/><circle cx="103" cy="17" r="14"/>
    </g>
    <g fill="none" stroke="#333" stroke-width="1">
      <rect x="13" y="10" width="8" height="14" rx="1.5"/>
      <rect x="53" y="11" width="14" height="11" rx="1"/><path d="M55 19h10"/>
      <path d="M97 11h12v12H97zM97 15h12M101 11v12"/>
    </g>
    <text x="38" y="19" font-size="6" fill="#333">+</text>
    <text x="81" y="19" font-size="6" fill="#333">+</text>
    <text x="122" y="19" font-size="6" fill="#333">=</text>
    <text x="132" y="16" font-size="5.2" font-weight="700" fill="#222" font-family="Montserrat,sans-serif">18 TONS OF CO2E /YEAR</text>
    <text x="139" y="23" font-size="5.2" font-weight="700" fill="#222" font-family="Montserrat,sans-serif">(AVERAGE USA)</text>
  </svg>
  <div class="abs small" style="left:0;right:0;top:132px;text-align:center;font-size:4.2px;color:#444">...provides nudges, points and financial incentives for reaching Net Zero Target</div>
  <svg class="abs" style="left:62px;top:144px" width="124" height="18" viewBox="0 0 124 18">
    <g fill="#222">
      <path d="M2 8l9-4 9 4-9 4z"/><rect x="8" y="10" width="6" height="4"/>
      <rect x="31" y="3" width="10" height="13" fill="none" stroke="#222"/>
      <path d="M56 14l12-11 2 2-11 11z"/>
      <rect x="80" y="2" width="10" height="14" fill="none" stroke="#222"/><path d="M82 13l6-8"/>
      <path d="M104 16l6-12 4 4-2 8z"/>
    </g>
  </svg>
  <div class="abs small" style="left:24px;right:24px;top:170px;text-align:center;font-size:4.2px;color:#444">Gamified behavioral science for carbon positive action across education, business, travel, policy &amp; lifestyle</div>
  <div class="card" style="left:16px;top:205px;width:216px;height:106px"></div>
  <svg class="abs" style="left:32px;top:222px" width="104" height="62" viewBox="0 0 104 62" role="img" aria-label="Bar chart of footprint by category">
    <rect width="104" height="62" fill="#1b6a5c"/>
    <g fill="#a7c93a"><rect x="8" y="14" width="9" height="36"/><rect x="27" y="30" width="9" height="20"/><rect x="47" y="10" width="9" height="40"/><rect x="67" y="22" width="9" height="28"/><rect x="87" y="18" width="9" height="32"/></g>
    <g font-size="3.2" fill="#fff" font-family="Montserrat,sans-serif"><text x="7" y="57">Food</text><text x="25" y="57">Shelter</text><text x="44" y="57">Mobility</text><text x="65" y="57">Goods</text><text x="83" y="57">Services</text></g>
  </svg>
  <div class="ph" style="left:150px;top:220px;width:68px;height:66px;border:2px solid #d6d8da;background:linear-gradient(180deg,#fff 0 8%,#4b4f5c 8%,#6b6f80 60%,#fff 60%)" role="img" aria-label="Phone screen with app notification"></div>
  <div class="abs" style="left:154px;top:268px;width:60px;height:14px;background:var(--teal);border-radius:2px;font-size:3px;color:#fff;text-align:center;padding-top:2px;line-height:1.3">Well done! Your logged reductions have earned you a bonus</div>
  <div class="foot"><div class="bar"></div><div class="url">www.marblequill.com</div><div class="brand">MarbleQuill</div></div>
</section>

<section class="page" style="left:476px;top:52px">
  <div class="mist"></div>
  <div class="head-bar"></div>
  <div class="head">We target systemic behavior change by applying gamification to the CSR / Employee Engagement Gap</div>
  <div class="tag"><i></i>Integrate</div>
  <div class="abs green bold" style="left:12px;top:47px;font-size:5.8px">MarbleQuill Enterprise 360 Net Zero Challenge:</div>
  <div class="abs" style="left:14px;top:66px;width:72px;height:82px;border:4px solid var(--orange);border-radius:6px;background:#fff"></div>
  <div class="abs" style="left:88px;top:66px;width:72px;height:82px;border:4px solid var(--royal);border-radius:6px;background:#fff"></div>
  <div class="abs" style="left:162px;top:66px;width:72px;height:82px;border:4px solid var(--lime);border-radius:6px;background:#fff"></div>
  <div class="abs tiny" style="left:20px;top:80px;width:60px;text-align:center"><b style="color:#222">SCALABLE</b><br><br>App model is user-friendly; provides superior sustainability data to CSR departments; modular for easy customizability</div>
  <div class="abs tiny" style="left:94px;top:80px;width:60px;text-align:center"><b style="color:#222">GAMIFIED</b><br><br>App model is user-friendly; provides superior sustainability data to CSR departments; modular for easy customizability</div>
  <div class="abs tiny" style="left:168px;top:80px;width:60px;text-align:center"><b style="color:#222">EFFECTIVE</b><br><br>Proven model for reducing emissions; lower operational costs, greener supply chain, improved employee morale, health outcomes, and brand reputation</div>
  <div class="card" style="left:14px;top:158px;width:218px;height:108px"></div>
  <div class="abs bold" style="left:0;right:0;top:172px;text-align:center;font-size:5px">IN 2017 WE REACHED 75K+ EMPLOYEES:</div>
  <div class="abs" style="left:0;right:0;top:180px;text-align:center;font-size:4px;color:#444">20 Top 500 organizations</div>
  <div class="chip" style="left:28px;top:194px;width:34px;height:12px;background:#e2a9a9"></div>
  <div class="chip" style="left:70px;top:196px;width:26px;height:10px;background:#9fb3d6"></div>
  <div class="chip" style="left:104px;top:194px;width:14px;height:14px;background:#8fc39a"></div>
  <div class="chip" style="left:126px;top:194px;width:22px;height:12px;background:#9fa9c9"></div>
  <div class="chip" style="left:158px;top:194px;width:26px;height:12px;background:#a9c9e6"></div>
  <div class="chip" style="left:34px;top:216px;width:12px;height:10px;background:#f2d28f"></div>
  <div class="chip" style="left:60px;top:216px;width:24px;height:8px"></div>
  <div class="chip" style="left:96px;top:216px;width:40px;height:8px;background:#e7aaa4"></div>
  <div class="chip" style="left:144px;top:216px;width:16px;height:8px;background:#a9b5cf"></div>
  <div class="chip" style="left:168px;top:214px;width:14px;height:12px;background:#b9d3ea"></div>
  <div class="chip" style="left:190px;top:214px;width:22px;height:12px"></div>
  <div class="chip" style="left:72px;top:236px;width:14px;height:14px;background:#b8d8b8"></div>
  <div class="chip" style="left:98px;top:238px;width:44px;height:10px"></div>
  <div class="chip" style="left:162px;top:238px;width:26px;height:10px;background:#e8d3a8"></div>
  <div class="abs" style="left:0;top:270px;width:246px;height:60px;background:#e3e4e5"></div>
  <div class="abs" style="left:12px;top:278px;font-size:3.6px;font-weight:600">...&amp; 100's of Non-profits and Schools</div>
  <div class="chip" style="left:12px;top:287px;width:15px;height:17px;background:#fff"></div>
  <div class="chip" style="left:30px;top:287px;width:24px;height:17px;background:#fff"></div>
  <div class="chip" style="left:57px;top:287px;width:18px;height:17px;background:#fff"></div>
  <div class="chip" style="left:78px;top:287px;width:18px;height:17px;background:#fff"></div>
  <div class="abs tiny" style="left:132px;top:274px;width:102px;text-align:right;color:#333">“Northbank sees great value in relationships that help us tap into employee motivation for fun, impactful, sustainability engagement - exactly what MarbleQuill offers.”<br><b>Priya Nandan,<br>Head of CSR at Northbank UK</b></div>
  <div class="foot"><div class="bar"></div><div class="url">www.marblequill.com</div><div class="brand">MarbleQuill</div></div>
</section>

<section class="page" style="left:779px;top:52px">
  <div class="mist"></div>
  <div class="head-bar"></div>
  <div class="head">Our platform matches Net Zero targets with scalable CO2 reduction projects</div>
  <div class="tag" style="color:var(--blue)"><i></i>Restore</div>
  <div class="abs green" style="left:0;right:0;top:58px;text-align:center;font-size:4.2px;font-weight:600">One-click access to select CO2 ‘clean-up’ projects to balance your carbon footprint</div>
  <div class="abs" style="left:11px;top:72px;width:226px;height:200px;background:#fff;border-radius:6px;box-shadow:0 1px 4px rgba(0,0,0,.12);overflow:hidden">
    <div class="abs" style="left:0;top:0;width:226px;height:20px;background:var(--blue)"></div>
    <div class="abs" style="left:0;top:5px;width:56px;text-align:center;font-size:4px;color:#fff;font-weight:600">Your Impact<br>Donation</div>
    <div class="abs" style="left:56px;top:8px;width:56px;text-align:center;font-size:4px;color:#fff;font-weight:600">Focus Areas</div>
    <div class="abs" style="left:112px;top:5px;width:56px;text-align:center;font-size:4px;color:#fff;font-weight:600">Implementing<br>Partners</div>
    <div class="abs" style="left:168px;top:8px;width:58px;text-align:center;font-size:4px;color:#fff;font-weight:600">Impact</div>
    <div class="abs tiny" style="left:6px;top:26px;width:48px;color:#444">Impact metrics offer choice for achieving CO2 neutrality<br><br>Simple, tax-deductible donation to verified projects<br><br>Exclusive stories &amp; VR content from the front-line of projects driving change<br><br>“Your $100 rainforest conservation donation cleared the remaining 9 tons of CO2 of your Net Zero target &amp; was matched by your employer. You are a carbon negative human.”</div>
    <div class="ph" style="left:57px;top:22px;width:55px;height:50px;border-radius:0;background:linear-gradient(160deg,#6fa53a,#2f6b22)" role="img" aria-label="Aerial view of forest"></div>
    <div class="ph" style="left:57px;top:74px;width:55px;height:50px;border-radius:0;background:linear-gradient(160deg,#7fd0ec,#1667a5)" role="img" aria-label="Ocean wave"></div>
    <div class="ph" style="left:57px;top:126px;width:55px;height:50px;border-radius:0;background:linear-gradient(160deg,#4e8ed0,#cfe3f4)" role="img" aria-label="Blue sky with clouds"></div>
    <div class="abs tiny" style="left:116px;top:40px;width:50px">Timberline<br>Focus on afforestation, conservation, and biochar</div>
    <div class="abs tiny" style="left:116px;top:90px;width:50px">Deepwater Foundation<br>Focus on ocean plastic clean-up and kelp/algae farming</div>
    <div class="abs tiny" style="left:116px;top:142px;width:50px">Airloop<br>Focus on direct-air-capture and mature clean grid tech</div>
    <div class="abs tiny" style="left:170px;top:40px;width:54px;text-align:center;color:#222">1 tree (40 years)<br>= ~1 tCO2<br>captured</div>
    <div class="abs tiny" style="left:170px;top:86px;width:54px;text-align:center;color:#222">1 acre of<br>seaweed =<br>Up to 68 tCO2 / yr</div>
    <div class="abs tiny" style="left:170px;top:136px;width:54px;text-align:center;color:#222">$94 - $232 /<br>tCO2<br>Filtrating CO2<br>out of the air</div>
    <div class="abs" style="left:112px;top:73px;width:114px;height:1px;background:#dde"></div>
    <div class="abs" style="left:112px;top:125px;width:114px;height:1px;background:#dde"></div>
    <div class="abs" style="left:57px;top:178px;width:169px;height:22px;background:var(--blue);font-size:3.5px;color:#fff;text-align:center;padding:6px 8px 0">MQ has and continues to develop partnership agreements with proven and high potential players in CO2 reduction</div>
  </div>
  <div class="foot"><div class="bar"></div><div class="url">www.marblequill.com</div><div class="brand">MarbleQuill</div></div>
</section>

<section class="page" style="left:175px;top:422px">
  <div class="mist"></div>
  <div class="head-bar"></div>
  <div class="head">Woven throughout MQ activities are experientials that inspire us to learn about, love, and care for our planet.</div>
  <div class="tag" style="color:var(--orange)"><i></i>Connect</div>
  <div class="abs green bold" style="left:22px;top:90px;font-size:7.4px;line-height:1.4">Global Climate<br>Leadership Expeditions</div>
  <div class="ph" style="left:134px;top:75px;width:94px;height:46px;background:linear-gradient(135deg,#a9c6d6,#5aa3c9 55%,#2c6f8e)" role="img" aria-label="Glacier and mountains"></div>
  <div class="card" style="left:15px;top:134px;width:215px;height:62px;overflow:hidden">
    <div class="abs" style="left:154px;top:0;width:61px;height:62px;background:var(--teal);font-size:3.6px;color:#fff;font-weight:600;padding:28px 0 0 12px">2+ HNWI / Expedition</div>
  </div>
  <div class="abs tiny" style="left:24px;top:140px;width:142px;color:#333"><b>3 Decades of experience leading climate leadership expeditions:</b><br>• Antarctica<br>• The Arctic<br><b>Strategic expansion to global climate hotspots and cutting edge Carbon Reduction Projects (2019e):</b><br>• Kilimanjaro<br>• Iceland &amp; Switzerland<br>• + many others from Restore Portfolio</div>
  <div class="card" style="left:15px;top:210px;width:70px;height:66px"></div>
  <div class="abs tiny" style="left:18px;top:218px;width:64px;text-align:center;color:#444">“Lessons from the Bottom of the World”<br>“Integrating Climate Solutions in your Everyday Life”<br>“Effective Fundraising for Good”</div>
  <div class="ph" style="left:88px;top:210px;width:70px;height:66px;background:linear-gradient(160deg,#6b6b6b,#1c1c1c)" role="img" aria-label="Speaker on stage at a keynote"></div>
  <div class="abs" style="left:88px;top:262px;width:70px;height:14px;background:var(--teal);color:#fff;font-size:4px;font-weight:600;text-align:center;padding-top:1px;line-height:1.3">Workshops and<br>Keynotes</div>
  <div class="ph" style="left:161px;top:210px;width:70px;height:66px;background:linear-gradient(160deg,#2f7fb0,#9ec6d8)" role="img" aria-label="Virtual reality headset"></div>
  <div class="abs" style="left:161px;top:262px;width:70px;height:14px;background:var(--teal);color:#fff;font-size:3.8px;font-weight:600;text-align:center;padding-top:1px;line-height:1.3">MarbleQuill Virtual<br>Reality Productions</div>
  <div class="foot"><div class="bar"></div><div class="url">www.marblequill.com</div><div class="brand">MarbleQuill</div></div>
</section>

<section class="page" style="left:476px;top:422px">
  <div class="mist"></div>
  <div class="head-bar" style="top:26px;height:12px"></div>
  <div class="head" style="top:28px">Our story</div>
  <div class="abs" style="left:16px;top:53px;width:214px;height:62px;background:#ececed;border-radius:4px"></div>
  <div class="abs tiny" style="left:24px;top:61px;width:198px;color:#444">After Edmund Hale became the first person to walk to both poles in 1989, Henri Marchal charged him with a 50 year mission to help preserve Antarctica through conservation and effective education - realized by the 7386 Foundation. The MarbleQuill Mission, spearheaded by his son Owen Hale, was built upon this 7386 legacy.<br><br>Through innovative ventures around the globe, the father and son team have been working side-by-side since 2011 to drive sustainable action between generations and cultures.</div>
  <div class="ph" style="left:24px;top:127px;width:70px;height:66px;background:linear-gradient(160deg,#c89a6e,#5a3a24)" role="img" aria-label="Portrait photo of Edmund Hale"></div>
  <div class="abs tiny" style="left:102px;top:139px;width:128px;color:#444;text-align:justify"><b style="color:#222">Edmund Hale OBE,</b><br>has dedicated his life to sustainable development, conservation, renewable energy, and education through the 7386 Foundation. He is focusing currently on speaking engagements and long distance cycling training.</div>
  <div class="ph" style="left:24px;top:201px;width:70px;height:67px;background:linear-gradient(160deg,#b7c4cc,#5f7684)" role="img" aria-label="Portrait photo of Owen Hale"></div>
  <div class="abs tiny" style="left:102px;top:210px;width:128px;color:#444;text-align:justify"><b style="color:#222">Owen Hale,</b><br>directs the MarbleQuill initiative with a passionate team across 4 continents. He led a two month ski to the South Pole - the first expedition of its kind powered exclusively on renewable energy. Some of his passions are gardening, sailing, and mountaineering.</div>
  <div class="foot"><div class="bar"></div><div class="url">www.marblequill.com</div><div class="brand">MarbleQuill</div></div>
</section>

<section class="page" style="left:779px;top:422px">
  <div class="ph" style="left:0;top:0;width:246px;height:349px;border-radius:0;background:linear-gradient(180deg,#ffffff 0%,#eef1f2 40%,#4d7482 52%,#2f5767 66%,#8fa7b3 75%,#3c6576 88%,#6d8b98 100%)" role="img" aria-label="Misty mountains above a lake"></div>
  <div class="head-bar" style="top:26px;height:12px"></div>
  <div class="head" style="top:28px">How to get involved</div>
  <div class="card" style="left:28px;top:60px;width:88px;height:47px;overflow:hidden">
    <div class="ph" style="left:2px;top:2px;width:84px;height:33px;border-radius:0;background:linear-gradient(180deg,#4b8ec9,#dfe8ef 70%,#fff)" role="img" aria-label="Polar bear on ice"></div>
    <div class="abs" style="left:2px;top:35px;width:84px;height:10px;background:var(--teal);color:#fff;font-size:4.6px;font-weight:600;text-align:center;padding-top:2px">Join Us up North</div>
  </div>
  <div class="card" style="left:130px;top:60px;width:88px;height:47px;overflow:hidden">
    <div class="ph" style="left:2px;top:2px;width:84px;height:33px;border-radius:0;background:linear-gradient(180deg,#c9d9e6,#f4f7f9)" role="img" aria-label="Skiers on a polar plain"></div>
    <div class="abs" style="left:2px;top:35px;width:84px;height:10px;background:var(--teal);color:#fff;font-size:4.6px;font-weight:600;text-align:center;padding-top:2px">Get in Touch</div>
  </div>
  <div class="foot"><div class="bar"></div><div class="url" style="color:#fff">www.marblequill.com</div><div class="brand" style="color:#fff">MarbleQuill</div></div>
</section>

<section class="page" style="left:175px;top:799px">
  <div class="abs" style="left:0;top:0;width:246px;height:349px;background:linear-gradient(180deg,#fff 0%,#fff 25%,#fbf1cf 45%,#efd98f 60%,#f3ead0 75%,#eeeeee 100%)"></div>
  <div class="head-bar"></div>
  <div class="head">“The greatest threat to our planet is the belief that someone else will save it.”</div>
  <div class="abs" style="left:12px;top:56px;font-size:11px;font-weight:500">Edmund Hale, OBE</div>
  <div class="abs" style="left:12px;top:80px;font-size:7.6px;line-height:1.5">APPENDIX<br>Our Theory of Change<br>5 Convenient Solutions: For Corporates</div>
  <div class="foot"><div class="bar"></div><div class="url">www.marblequill.com</div><div class="brand">MarbleQuill</div></div>
</section>

<section class="page" style="left:476px;top:799px">
  <div class="mist"></div>
  <div class="head-bar" style="top:26px;height:12px"></div>
  <div class="head" style="top:28px">Our theory of change</div>
  <svg class="abs" style="left:16px;top:82px" width="216" height="26" viewBox="0 0 216 26">
    <g font-family="Montserrat,sans-serif" font-size="4" font-weight="600" fill="#fff" text-anchor="middle">
      <path d="M0 0h44l10 13-10 13H0l10-13z" fill="#8e2fb8"/><text x="28" y="14.5">Activities</text>
      <path d="M54 0h44l10 13-10 13H54l10-13z" fill="#1e9b57"/><text x="82" y="11">Outputs</text><text x="82" y="16">(End of 2019)</text>
      <path d="M108 0h44l10 13-10 13h-44l10-13z" fill="#f3a51c"/><text x="136" y="14.5">Outcomes</text>
      <path d="M162 0h44l10 13-10 13h-44l10-13z" fill="#e5472f"/><text x="190" y="14.5">Impact</text>
    </g>
  </svg>
  <div class="card" style="left:18px;top:130px;width:50px;height:46px;font-size:5.4px;text-align:center;padding-top:19px">Integrate</div>
  <div class="card" style="left:18px;top:180px;width:50px;height:46px;font-size:5.4px;text-align:center;padding-top:19px">Restore</div>
  <div class="card" style="left:18px;top:230px;width:50px;height:46px;font-size:5.4px;text-align:center;padding-top:19px">Connect</div>
  <div class="card tiny" style="left:72px;top:130px;width:52px;height:46px;padding:6px 4px;text-align:center">Deliver current, digestible sustainable living content and solutions to 1 million people through social engagement platforms</div>
  <div class="card tiny" style="left:72px;top:180px;width:52px;height:46px;padding:6px 4px;text-align:center">Galvanize 2 million dollars towards proven and emerging carbon-negative solutions</div>
  <div class="card tiny" style="left:72px;top:230px;width:52px;height:46px;padding:6px 4px;text-align:center">Convene and train 700 future environmental leaders through immersive, pro-environment experiences locally and globally</div>
  <div class="card tiny" style="left:127px;top:130px;width:52px;height:46px;padding:6px 4px;text-align:center">Individuals and organizations drive and demand sustainable practices across 5 key social sectors</div>
  <div class="card tiny" style="left:127px;top:180px;width:52px;height:46px;padding:6px 4px;text-align:center">Individuals and organizations easily and routinely offset their carbon footprint; emerging carbon-negative solutions reach maturity</div>
  <div class="card tiny" style="left:127px;top:230px;width:52px;height:46px;padding:6px 4px;text-align:center">Tight network of global change leaders embed sustainability practices at home and in the marketplace</div>
  <div class="card" style="left:182px;top:130px;width:48px;height:146px;font-size:5px;text-align:center;padding-top:62px;line-height:1.3">360 million tons of CO2 offset by 2025</div>
  <div class="foot"><div class="bar"></div><div class="url">www.marblequill.com</div><div class="brand">MarbleQuill</div></div>
</section>

<section class="page" style="left:779px;top:799px">
  <div class="mist"></div>
  <div class="head-bar" style="top:26px;height:12px"></div>
  <div class="head" style="left:16px;top:28px;font-size:5.8px">Convenient Solutions from MarbleQuill</div>
  <div class="abs green bold" style="left:16px;top:46px;font-size:5.6px;line-height:1.4">5 Solutions businesses and busy people can integrate<br>in their day-to-day</div>
  <div class="abs tiny" style="left:16px;top:78px;width:124px;color:#444">Reduce your impact: did you know refrigerant management is the #1 sector to go carbon neutral? Tips and products to save $ and the whales<br><br>Offset: access our high-quality portfolio of afforestation and conservation projects. Globally accredited, expertly curated.<br><br>Negative Emissions Technologies: donate to cutting-edge projects in direct-air capture, algae-farming, and more. Imperative to meet Paris.<br><br>Invest Ethically: achieve environmental returns through our socially responsible investing (SRI) financial partners. Green is green<br><br>Measure your footprint: with our carbon tracking solutions for business and individuals. What doesn't get measured doesn't get managed</div>
  <div class="ph" style="left:160px;top:80px;width:52px;height:52px;border-radius:50%;background:radial-gradient(circle,#f0a85a 0 25%,#2c6fb3 26% 100%)" role="img" aria-label="Illustration of app connecting everyday activities"></div>
  <div class="abs tiny" style="left:148px;top:138px;width:76px;text-align:center;color:#444">The Connector App (in dev)<br>Tracks your carbon<br>Customized advice<br>Easy offsets<br>Gamification incentivizes community behavior shift</div>
  <div class="abs bold" style="left:0;right:0;top:212px;text-align:center;font-size:6px;line-height:1.4">THE GOAL: MOBILIZE THE REDUCTION OF<br>360 MILLION TONS OF CO2 BY 2025</div>
  <div class="foot"><div class="bar"></div><div class="url">www.marblequill.com</div><div class="brand">MarbleQuill</div></div>
</section>

</div>
</body>
</html>
```